Creative Design "Size Chart" for a Clothing Product

Hi, My dear friends! I am looking to do a contest to design a unique creative "Size Chart" for our clothing line. See Attached the Sizes & Ideas Thanks Good Luck Osvald

Colors

Designer to choose colors to be used in the design.

```html
<!DOCTYPE html>
<html lang="en">
<head>
<meta charset="utf-8">
<title>Size Specification Charts</title>
<link href="https://fonts.googleapis.com/css2?family=Catamaran:wght@500;600;700;800&display=swap" rel="stylesheet">
<style>
  :root {
    --men-dark: #0358a9;
    --men-light: #a9dbf6;
    --men-pale: #c9e8fa;
    --men-cell: #5ea7dd;
    --women-dark: #c11f80;
    --women-light: #ecc6dc;
    --women-pale: #f6dded;
    --women-cell: #d17cb8;
    --boys-dark: #00a596;
    --boys-light: #b5e0d6;
    --boys-pale: #d6eee8;
    --boys-cell: #38bfb0;
    --girls-dark: #dd6535;
    --girls-light: #f9c3a0;
    --girls-pale: #fcdac3;
    --girls-cell: #f38d59;
    --white: #ffffff;
  }
  * { box-sizing: border-box; margin: 0; padding: 0; }
  html, body { width: 1200px; height: 649px; overflow: hidden; background: var(--white); }
  body { position: relative; font-family: "Catamaran", sans-serif; }

  .chart {
    position: absolute;
    width: 595px;
    height: 320px;
    border: 6px solid var(--dark);
    background: linear-gradient(115deg, var(--pale) 0%, var(--pale) 55%, var(--light) 55%, var(--light) 100%);
    overflow: hidden;
  }
  .chart--men   { left: 0;   top: 0;   --dark: var(--men-dark);   --light: var(--men-light);   --pale: var(--men-pale);   --cell: var(--men-cell); }
  .chart--women { left: 605px; top: 0;   --dark: var(--women-dark); --light: var(--women-light); --pale: var(--women-pale); --cell: var(--women-cell); }
  .chart--boys  { left: 0;   top: 329px; --dark: var(--boys-dark);  --light: var(--boys-light);  --pale: var(--boys-pale);  --cell: var(--boys-cell); }
  .chart--girls { left: 605px; top: 329px; --dark: var(--girls-dark); --light: var(--girls-light); --pale: var(--girls-pale); --cell: var(--girls-cell); }

  .chart__header {
    position: absolute;
    left: -6px; top: -6px;
    width: 595px; height: 50px;
    background: var(--dark);
    clip-path: polygon(0 0, 89.5% 0, 85% 100%, 0 100%);
  }
  .chart__title {
    position: absolute;
    left: 0; top: 8px;
    width: 520px;
    text-align: center;
    color: var(--white);
    font-weight: 800;
    font-size: 16.5px;
    letter-spacing: 1.3px;
    line-height: 30px;
  }

  .size-table {
    position: absolute;
    left: 27px;
    top: 64px;
    width: 308px;
    border-collapse: collapse;
  }
  .chart--women .size-table { top: 56px; }
  .size-table th, .size-table td {
    width: 33.33%;
    text-align: center;
    border: 1.5px solid rgba(255,255,255,0.75);
  }
  .size-table th {
    background: var(--white);
    color: var(--dark);
    font-weight: 500;
    font-size: 18.5px;
    height: 38px;
    line-height: 38px;
  }
  .size-table td {
    background: var(--cell);
    color: var(--white);
    font-weight: 600;
    font-size: 11.5px;
    height: 28.6px;
    line-height: 28px;
  }

  .garment {
    position: absolute;
    border-radius: 14px 14px 8px 8px;
    background: linear-gradient(180deg, rgba(255,255,255,0.85), rgba(255,255,255,0.6));
    border: 1.5px solid var(--dark);
  }
  .chart--men .garment   { left: 370px; top: 66px; width: 175px; height: 212px; }
  .chart--women .garment { left: 370px; top: 58px; width: 175px; height: 232px; }
  .chart--boys .garment  { left: 355px; top: 92px; width: 185px; height: 172px; }
  .chart--girls .garment { left: 375px; top: 94px; width: 170px; height: 172px; }
</style>
</head>
<body>

<section class="chart chart--men">
  <div class="chart__header"></div>
  <h2 class="chart__title">MENS SIZE SPECIFICATION CHART</h2>
  <table class="size-table">
    <thead><tr><th>Size</th><th>Chest</th><th>Waist</th></tr></thead>
    <tbody>
      <tr><td>Small</td><td>34-36</td><td>28-30</td></tr>
      <tr><td>Medium</td><td>36-38</td><td>30-32</td></tr>
      <tr><td>Large</td><td>38-40</td><td>32-34</td></tr>
      <tr><td>X Large</td><td>40-42</td><td>34-36</td></tr>
      <tr><td>2X Large</td><td>43-45</td><td>36-40</td></tr>
      <tr><td>3X Large</td><td>45-48</td><td>40-44</td></tr>
    </tbody>
  </table>
  <div class="garment" role="img" aria-label="Illustration of a men's t-shirt with chest and waist measurement lines"></div>
</section>

<section class="chart chart--women">
  <div class="chart__header"></div>
  <h2 class="chart__title">WOMENS SIZE SPECIFICATION CHART</h2>
  <table class="size-table">
    <thead><tr><th>Size</th><th>Chest</th><th>Waist</th></tr></thead>
    <tbody>
      <tr><td>X Small (0-2)</td><td>32-34</td><td>26-28</td></tr>
      <tr><td>Small (4-6)</td><td>34-36</td><td>28-30</td></tr>
      <tr><td>Medium (8-10)</td><td>36-38</td><td>30-32</td></tr>
      <tr><td>Large (12-14)</td><td>38-40</td><td>32-34</td></tr>
      <tr><td>X Large (14-16)</td><td>40-42</td><td>34-36</td></tr>
      <tr><td>2X Large (18)</td><td>42-44</td><td>36-38</td></tr>
      <tr><td>3X Large (20)</td><td>44-46</td><td>38-40</td></tr>
    </tbody>
  </table>
  <div class="garment" role="img" aria-label="Illustration of a women's fitted t-shirt with chest and waist measurement lines"></div>
</section>

<section class="chart chart--boys">
  <div class="chart__header"></div>
  <h2 class="chart__title">BOYS SIZE SPECIFICATION CHART</h2>
  <table class="size-table">
    <thead><tr><th>Size</th><th>Chest</th><th>Waist</th></tr></thead>
    <tbody>
      <tr><td>XX Small</td><td>20-23</td><td>19-21</td></tr>
      <tr><td>X Small</td><td>23-26</td><td>21-23</td></tr>
      <tr><td>Small</td><td>26-29</td><td>23-25</td></tr>
      <tr><td>Medium</td><td>29-32</td><td>25-27</td></tr>
      <tr><td>Large</td><td>32-35</td><td>27-29</td></tr>
      <tr><td>X Large</td><td>35-38</td><td>29-31</td></tr>
    </tbody>
  </table>
  <div class="garment" role="img" aria-label="Illustration of a boys' t-shirt with chest and waist measurement lines"></div>
</section>

<section class="chart chart--girls">
  <div class="chart__header"></div>
  <h2 class="chart__title">GIRLS SIZE SPECIFICATION CHART</h2>
  <table class="size-table">
    <thead><tr><th>Size</th><th>Chest</th><th>Waist</th></tr></thead>
    <tbody>
      <tr><td>XX Small</td><td>19-22</td><td>18-20</td></tr>
      <tr><td>X Small</td><td>22-25</td><td>20-22</td></tr>
      <tr><td>Small</td><td>25-28</td><td>22-24</td></tr>
      <tr><td>Medium</td><td>28-31</td><td>24-26</td></tr>
      <tr><td>Large</td><td>31-34</td><td>26-28</td></tr>
      <tr><td>X Large</td><td>34-37</td><td>28-30</td></tr>
    </tbody>
  </table>
  <div class="garment" role="img" aria-label="Illustration of a girls' t-shirt with chest and waist measurement lines"></div>
</section>

</body>
</html>
```